WE WOULD LIKE TO HAVE PROFESSIONAL LOOK ALLERGEN MATRIX DESIGN.
Our company is KANDRIX VENTURES LIMITED.
I am sharing a competitors design as well.
We would like to have grafics for 14 allergens. At the end of the allergen matrix we would like to have a like a list for review details and approval date. I am also attaching an example what we are using right now.
We would like to signs for may contain, contains, removable, additionally GMO and Colorant

```html
<!DOCTYPE html>
<html lang="en">
<head>
<meta charset="utf-8">
<title>Kandrix Ventures Limited – Allergen Matrix</title>
<link href="https://fonts.googleapis.com/css2?family=Montserrat:wght@300;500&family=Crimson+Text:wght@600;700&display=swap" rel="stylesheet">
<style>
  :root {
    --page-bg: #8a8a8a;
    --card-bg: #ffffff;
    --lime: #c3cf2f;
    --ink: #111111;
    --panel-grey: #e9e9e9;
    --alert-red: #e2262b;
    --white: #ffffff;
  }
  * { box-sizing: border-box; margin: 0; padding: 0; }
  html, body { width: 990px; height: 1200px; overflow: hidden; background: var(--page-bg); }

  .card {
    position: absolute;
    left: 30px; top: 347px;
    width: 1470px; height: 800px;
    background: var(--card-bg);
    transform: scale(0.6327);
    transform-origin: top left;
    box-shadow: 0 4px 14px rgba(0,0,0,0.25);
    font-family: "Crimson Text", Georgia, serif;
    color: var(--ink);
  }

  .brand-name {
    position: absolute; left: 57px; top: 68px;
    font-family: "Montserrat", Arial, sans-serif;
    font-weight: 500; font-size: 64px; letter-spacing: 9px;
    line-height: 1;
  }
  .brand-divider {
    position: absolute; left: 452px; top: 70px;
    width: 2px; height: 68px; background: var(--ink);
  }
  .brand-tagline {
    position: absolute; left: 472px; top: 72px;
    font-family: "Montserrat", Arial, sans-serif;
    font-weight: 300; font-size: 25px; letter-spacing: 5px;
    line-height: 34px;
  }
  .title-panel {
    position: absolute; left: 799px; top: 53px;
    width: 612px; height: 92px; background: var(--panel-grey);
  }

  .section-tab {
    position: absolute; left: 606px; top: 188px;
    width: 399px; height: 76px;
    background: var(--lime);
    border-radius: 32px 32px 0 0;
    font-weight: 700; font-size: 50px;
    text-align: center; line-height: 82px;
    letter-spacing: 0.5px;
  }

  .matrix {
    position: absolute; left: 60px; top: 262px;
    width: 1347px; height: 463px;
    border: 1.5px solid var(--lime);
    border-radius: 16px;
    overflow: hidden;
    display: grid;
    grid-template-columns: 145px repeat(15, 80px);
    grid-template-rows: 126px 100px 10px 54px 1fr;
  }

  .legend { grid-column: 1; grid-row: 1 / 3; padding: 10px 0 0 10px; }
  .legend-item {
    display: flex; align-items: flex-start; gap: 8px;
    font-weight: 600; font-size: 12.5px; line-height: 15px;
    margin-bottom: 16px;
  }
  .marker {
    flex: none; width: 15px; height: 15px; border-radius: 50%;
    background: var(--alert-red); color: var(--white);
    font-family: Arial, sans-serif; font-weight: 700; font-size: 8px;
    display: flex; align-items: center; justify-content: center;
  }
  .marker svg { width: 9px; height: 9px; }

  .icon-cell {
    grid-row: 1; border-left: 1px solid var(--lime);
    display: flex; align-items: center; justify-content: center;
  }
  .allergen-icon {
    width: 62px; height: 62px; border-radius: 50%;
    background: var(--ink); border: 3px solid var(--lime);
  }

  .label-cell {
    grid-row: 2; background: var(--lime);
    border-left: 1px solid var(--white);
    display: flex; align-items: center; justify-content: center;
    text-align: center; font-weight: 600; font-size: 13px; line-height: 15px;
  }
  .label-cell:first-of-type { border-left: none; }

  .band-spacer { grid-row: 3; grid-column: 1 / -1; }

  .menu-band {
    grid-row: 4; grid-column: 1 / -1;
    background: var(--ink); color: var(--white);
    font-weight: 700; font-size: 31px;
    display: flex; align-items: center; justify-content: center;
    letter-spacing: 0.5px;
  }

  .dish-name {
    grid-row: 5; grid-column: 1;
    padding: 22px 0 0 28px;
    font-weight: 700; font-size: 15px;
  }
  .dish-cell {
    grid-row: 5; border-left: 1px solid var(--lime);
    padding: 18px 0 0 10px;
  }
  .dish-entry {
    display: flex; align-items: center; gap: 5px;
    font-weight: 600; font-size: 12.5px; height: 23.5px;
  }
  .dish-entry .marker { width: 14px; height: 14px; }
  .dish-stack { display: flex; flex-direction: column; gap: 3px; }
</style>
</head>
<body>
<main class="card">
  <div class="brand-name">KANDRIX</div>
  <div class="brand-divider"></div>
  <div class="brand-tagline">FOOD HYGIENE<br>HEALTH &amp; SAFETY</div>
  <div class="title-panel"></div>

  <div class="section-tab">MENU DISHES</div>

  <section class="matrix">
    <div class="legend">
      <div class="legend-item"><span class="marker">M</span>May Contain</div>
      <div class="legend-item"><span class="marker"><svg viewBox="0 0 10 10"><path d="M2 5.2 L4.2 7.4 L8 2.8" fill="none" stroke="#fff" stroke-width="1.8"/></svg></span>Contains</div>
      <div class="legend-item"><span class="marker">R</span>Removable</div>
      <div class="legend-item"><span class="marker"><svg viewBox="0 0 10 10"><path d="M2.5 7.5 L7.5 2.5" stroke="#fff" stroke-width="1.8" stroke-linecap="round"/></svg></span>Additionally GMO<br>And Colorant</div>
    </div>

    <div class="icon-cell" style="grid-column:2"></div>
    <div class="icon-cell" style="grid-column:3"><div class="allergen-icon" role="img" aria-label="Celery icon"></div></div>
    <div class="icon-cell" style="grid-column:4"><div class="allergen-icon" role="img" aria-label="Cereals containing gluten icon"></div></div>
    <div class="icon-cell" style="grid-column:5"><div class="allergen-icon" role="img" aria-label="Crustaceans icon"></div></div>
    <div class="icon-cell" style="grid-column:6"><div class="allergen-icon" role="img" aria-label="Eggs icon"></div></div>
    <div class="icon-cell" style="grid-column:7"><div class="allergen-icon" role="img" aria-label="Fish icon"></div></div>
    <div class="icon-cell" style="grid-column:8"><div class="allergen-icon" role="img" aria-label="Lupin icon"></div></div>
    <div class="icon-cell" style="grid-column:9"><div class="allergen-icon" role="img" aria-label="Milk icon"></div></div>
    <div class="icon-cell" style="grid-column:10"><div class="allergen-icon" role="img" aria-label="Molluscs icon"></div></div>
    <div class="icon-cell" style="grid-column:11"><div class="allergen-icon" role="img" aria-label="Mustard icon"></div></div>
    <div class="icon-cell" style="grid-column:12"><div class="allergen-icon" role="img" aria-label="Peanuts icon"></div></div>
    <div class="icon-cell" style="grid-column:13"><div class="allergen-icon" role="img" aria-label="Sesame seeds icon"></div></div>
    <div class="icon-cell" style="grid-column:14"><div class="allergen-icon" role="img" aria-label="Soya icon"></div></div>
    <div class="icon-cell" style="grid-column:15"><div class="allergen-icon" role="img" aria-label="Sulphur dioxide icon"></div></div>
    <div class="icon-cell" style="grid-column:16"><div class="allergen-icon" role="img" aria-label="Tree nuts icon"></div></div>

    <div class="label-cell" style="grid-column:2">No<br>Allergen</div>
    <div class="label-cell" style="grid-column:3">Celery<br>And<br>Celerac</div>
    <div class="label-cell" style="grid-column:4">Cereals<br>Containing<br>Gluten</div>
    <div class="label-cell" style="grid-column:5">Crustaceans</div>
    <div class="label-cell" style="grid-column:6">Eggs</div>
    <div class="label-cell" style="grid-column:7">Fish</div>
    <div class="label-cell" style="grid-column:8">Lupin</div>
    <div class="label-cell" style="grid-column:9">Milk</div>
    <div class="label-cell" style="grid-column:10">Molluscs</div>
    <div class="label-cell" style="grid-column:11">Mustard</div>
    <div class="label-cell" style="grid-column:12">Peanuts</div>
    <div class="label-cell" style="grid-column:13">Sesame<br>Seeds</div>
    <div class="label-cell" style="grid-column:14">Soya</div>
    <div class="label-cell" style="grid-column:15">Sulphur<br>Dioxide<br>(Sulphites)</div>
    <div class="label-cell" style="grid-column:16">Tree Nuts</div>

    <div class="band-spacer"></div>
    <div class="menu-band">Christmas Menu</div>

    <div class="dish-name">Roast Potatoes</div>
    <div class="dish-cell" style="grid-column:2"></div>
    <div class="dish-cell" style="grid-column:3">
      <div class="dish-entry"><span class="marker">M</span>Bakery</div>
      <div class="dish-entry"><span class="marker">M</span>Kamul</div>
      <div class="dish-entry"><span class="marker">M</span>Cuts</div>
      <div class="dish-entry"><span class="marker">M</span>Fry</div>
      <div class="dish-entry"><span class="marker">M</span>Spelt</div>
      <div class="dish-entry"><span class="marker"><svg viewBox="0 0 10 10"><path d="M2 5.2 L4.2 7.4 L8 2.8" fill="none" stroke="#fff" stroke-width="1.8"/></svg></span>Wheat</div>
    </div>
    <div class="dish-cell" style="grid-column:4"></div>
    <div class="dish-cell" style="grid-column:5"></div>
    <div class="dish-cell" style="grid-column:6"></div>
    <div class="dish-cell" style="grid-column:7"></div>
    <div class="dish-cell" style="grid-column:8"></div>
    <div class="dish-cell" style="grid-column:9"></div>
    <div class="dish-cell" style="grid-column:10"></div>
    <div class="dish-cell" style="grid-column:11"></div>
    <div class="dish-cell" style="grid-column:12"></div>
    <div class="dish-cell" style="grid-column:13"></div>
    <div class="dish-cell" style="grid-column:14"></div>
    <div class="dish-cell" style="grid-column:15"></div>
    <div class="dish-cell" style="grid-column:16; padding-left:5px">
      <div class="dish-entry" style="height:16px"><span class="marker"><svg viewBox="0 0 10 10"><path d="M2 5.2 L4.2 7.4 L8 2.8" fill="none" stroke="#fff" stroke-width="1.8"/></svg></span>Almonds</div>
      <div class="dish-entry" style="height:16px"><span class="marker">R</span></div>
    </div>
  </section>
</main>
</body>
</html>
```